Cafe - A FRAME Design

Need to create an A frame for my café.
Logo available
Word document - has basic information we think would be good.

Name: Zorvette Café

Notes from the A-frame printers.
File Requirements
• PDF without trim, crop or registration marks
• All files to be CMYK, not RGB
• All fonts converted to outlines (paths/curves)
• Embed all images and elements
• Files to be 100% scale unless otherwise specified
• 10mm Bleed
Resolution
• Bitmap images no less than 130 DPI at full size
Pantone Colours
• If required Pantone colours must be supplied

Target Market(s)

Mainly Students - University cafe

Requirements
Must have
• Cafe name: Zorvette
Nice to have
• Might be nice to have background - that orange color same as logo - just an idea

Word document - has basic idea regarding text that should be included

```html
<!DOCTYPE html>
<html lang="en">
<head>
<meta charset="utf-8">
<title>Zorvette Café – A-Frame</title>
<link rel="stylesheet" href="https://fonts.googleapis.com/css2?family=Bebas+Neue&family=Montserrat:wght@700&family=Playfair+Display:wght@900&display=swap">
<style>
  :root {
    --tan: #d4aa67;
    --orange: #f15f24;
    --slate: #484b55;
    --peach: #fcc08e;
    --white: #ffffff;
    --art-tone: rgba(72, 75, 85, 0.28);
  }
  * { margin: 0; padding: 0; box-sizing: border-box; }
  html, body { width: 800px; height: 1200px; overflow: hidden; background: var(--orange); }
  .aframe { position: relative; width: 800px; height: 1200px; background: var(--orange); overflow: hidden; }

  .brand-band { position: absolute; left: 0; top: 0; width: 800px; height: 325px; background: var(--tan); }
  .brand-dot { position: absolute; left: 350px; top: 50px; width: 100px; height: 100px; border-radius: 50%; background: var(--orange); }
  .brand-name {
    position: absolute; left: 0; top: 222px; width: 800px; text-align: center;
    font-family: "Montserrat", sans-serif; font-weight: 700; font-size: 66px;
    color: var(--slate); letter-spacing: -1px; line-height: 1;
  }

  .tagline-box {
    position: absolute; left: 28px; top: 345px; width: 743px; height: 243px;
    background: var(--slate); border-radius: 14px;
    display: flex; flex-direction: column; justify-content: center; align-items: center;
    font-family: "Playfair Display", serif; font-weight: 900; color: var(--white);
    text-align: center; white-space: nowrap;
  }
  .tagline-line--top { font-size: 70px; line-height: 1; letter-spacing: -2px; }
  .tagline-amp { font-size: 60px; line-height: 1.05; }
  .tagline-line--bottom { font-size: 59px; line-height: 1.1; letter-spacing: -1.5px; }

  .offer-list {
    position: absolute; left: 0; top: 627px; width: 800px; list-style: none; text-align: center;
    font-family: "Bebas Neue", sans-serif; font-size: 66px; line-height: 84.5px; color: var(--peach);
    white-space: nowrap;
  }

  .art { position: absolute; background: var(--art-tone); border-radius: 12px; }
  .art-mug { left: 80px; top: 616px; width: 127px; height: 112px; }
  .art-spoon { left: 88px; top: 741px; width: 108px; height: 129px; }
  .art-moka { left: 603px; top: 646px; width: 138px; height: 217px; }
  .art-beans { left: 650px; top: 955px; width: 98px; height: 88px; }

  .location-band {
    position: absolute; left: 0; top: 1063px; width: 800px; height: 137px; background: var(--slate);
    display: flex; align-items: center; justify-content: center;
    font-family: "Bebas Neue", sans-serif; font-size: 66px; color: var(--peach); padding-top: 6px;
  }
</style>
</head>
<body>
<main class="aframe">
  <header class="brand-band">
    <div class="brand-dot"></div>
    <div class="brand-name">Zorvette</div>
  </header>

  <section class="tagline-box">
    <p class="tagline-line--top">Your environmentally</p>
    <p class="tagline-amp">&amp;</p>
    <p class="tagline-line--bottom">sustainability focused cafe</p>
  </section>

  <div class="art art-mug" role="img" aria-label="Line drawing of a tea mug with a teabag tag"></div>
  <div class="art art-spoon" role="img" aria-label="Drawing of a spoon"></div>
  <div class="art art-moka" role="img" aria-label="Line drawing of a stovetop moka coffee pot"></div>
  <div class="art art-beans" role="img" aria-label="Line drawing of two coffee beans"></div>

  <ul class="offer-list">
    <li>Specialty Coffee</li>
    <li>Fresh Food</li>
    <li>Pastries &amp; Drinks</li>
    <li>(Vegan &amp; GF) Options Available</li>
    <li>Catering Available</li>
  </ul>

  <footer class="location-band">Located @ Building 418</footer>
</main>
</body>
</html>
```